Book Cover for a book on Lantern Road Ventures

I am self-publishing my book on Brindlemark and need a book cover made. Below are the details. See attached templates for size we need to use. I also attached a previous cover we had made that I liked. The problem with it was they were two boys helping each other but the book is about women. I'm open to your ideas on the cover though, but I wanted to show you a style I liked as an idea.
Front of Cover
Book Title: Lantern Road Ventures
Book Subtitle: Loose Pages of a Harbor Keeper
Author Name: Mirela T. Dunbar
Add on the Spine of Cover: Lantern Road Ventures and Mirela T. Dunbar
Back of the Cover Text:
Lantern Road Ventures: Loose Pages of a Harbor Keeper is an honest account of a business owner’s experience attempting to navigate the start-up community while also pursuing spiritual growth. Author Mirela Dunbar defines a spiritual entrepreneur as “someone who runs an enterprise with the purpose of growing love rather than material gain.” This book discusses the three dimensions of Lantern Road Ventures:
1. The business is an integral part of the founder’s spiritual journey.
2. Employees working for the spiritual enterprise, whether they know it or not, encounter this company because it's part of their spiritual path.
3. The business itself has a life force of its own and its purpose is to further the kingdom of heaven on earth.
These three dimensions happen simultaneously and work together to produce the greatest possible result. However, this can feel confusing to a founder juggling these dimensions while also trying to manage and run a business. This is not a formulaic self-help book or roadmap. Rather, it is a compilation of personal reflections that often seem at odds with the traditional world of entrepreneurship.
Below the description add my picture (see attached for my picture)
Bio text:
Mirela Dunbar founded Calveta with the vision of ushering in a life-long education system that shifts away from standardization to one that empowers people to live their purpose. In college, Mirela interned for Open Kettle, a women’s empowerment initiative where she recognized her passion for helping people find their voice. Mirela's 20-year journey has come full circle to empowering other female CEOs who are pursuing the path of Lantern Road Ventures.
NOTE: Please note that Brindlemark puts a bar code on the bottom right of the back cover as is noted on the attached template.
Size template is attached to the brief, here are the sizes typed out:
# Description Width (in) Height (in)
1 Full Cover 12.79 9.25
2 Front Cover 6 9
3 Safe Area 5.875 8.75
4 Bleed 0.125 0.125
5 Margin 0.125 0.125
6 Spine 0.54 9
7 Spine Safe Area 0.415 8.75
8 Spine Margin 0.062 0.062
9 Barcode Margin 0.25 0.25
Pre-publication checklist
BRINDLEMARK TIPS for the final cover:
1. Save as a PDF. Your cover must be a single PDF that includes the back cover, spine, and front cover as one image.
2. Flatten all transparencies. These can cause the file to print with missing or distorted content. Consult your software's documentation to learn how.
3. Embed your fonts. Consult your software's documentation to learn how.
4. Remove crop marks, color bars, template text. Crop marks are lines showing where pages should be trimmed. Color bars are strips with a series of patches used to ensure color balance during printing. Also, remove any template text, PDF creation guides, or software references.
5. Ensure your cover image meets the minimum resolution of 300 DPI (dots per inch).
6. Optimize PDFs. Optimization is useful to reduce your file size, allowing for higher performance when transferring, uploading, viewing, and printing the files.
7. Remove file security. Locked or encrypted files will fail review.
Target Market(s)
Women who want to be CEOs or are currently CEOs of companies.
Industry/Entity Type
Entrepreneurship, business, spirituality
Requirements
Must have
- Just the text on the description. A very welcoming feel.
Nice to have
- I like the idea of having a sunrise/sunset in the image somehow like in the example I attached to the brief, but again I'm open.
Should not have
- Please don't put any yoga or meditation poses or hands outstretched. I have a lot of interesting ones that look like my example so if you are going to submit after Saturday 10/29, please only do so if you have a new idea! Thanks!

```html
<!DOCTYPE html>
<html lang="en">
<head>
<meta charset="utf-8">
<title>Lantern Road Ventures — Book Cover</title>
<link href="https://fonts.googleapis.com/css2?family=Allison&family=Cormorant+Garamond:wght@500;600&family=Tinos&display=swap" rel="stylesheet">
<style>
  :root {
    --ink: #000000;
    --paper: #ffffff;
    --sky-blue: #8ec5f7;
    --sky-deep: #2c5a9e;
    --sky-mid: #6f9ccc;
    --sky-light: #d6e4f1;
    --body: #f2f2f2;
  }
  * { margin: 0; padding: 0; box-sizing: border-box; }
  html, body { width: 1200px; height: 868px; overflow: hidden; background: var(--ink); }
  .cover { position: relative; width: 1200px; height: 868px; background: var(--ink); color: var(--paper); }

  .script { font-family: "Allison", cursive; color: var(--sky-blue); font-weight: 400; line-height: 1; white-space: nowrap; }
  .caps { font-family: "Cormorant Garamond", serif; font-weight: 500; letter-spacing: 0.08em; white-space: nowrap; }

  /* Back cover */
  .back { position: absolute; left: 0; top: 0; width: 624px; height: 868px; }
  .back-title { position: absolute; left: 0; width: 590px; top: 48px; text-align: center; }
  .back-title .script { font-size: 78px; }
  .back-title .caps { font-size: 18px; margin-top: 2px; letter-spacing: 0.1em; }
  .blurb { position: absolute; left: 62px; width: 463px; top: 187px; font-family: "Tinos", serif; font-size: 11.6px; line-height: 19.6px; color: var(--body); text-align: justify; }
  .blurb .lead { color: var(--sky-blue); }
  .blurb p { margin-bottom: 14px; }
  .blurb ol { list-style: none; margin-bottom: 14px; }
  .blurb ol li { padding-left: 11px; text-indent: -11px; text-align: left; }
  .author-photo { position: absolute; left: 62px; top: 545px; width: 122px; height: 151px; background: linear-gradient(160deg, #8fb07a 0%, #5f8a4e 45%, #e0546f 100%); }
  .bio { position: absolute; left: 202px; width: 322px; top: 541px; font-family: "Tinos", serif; font-size: 11.6px; line-height: 19.6px; color: var(--body); text-align: justify; }

  /* Spine */
  .spine { position: absolute; left: 580px; top: 48px; width: 44px; height: 770px; display: flex; align-items: center; }
  .spine-text { writing-mode: vertical-rl; display: flex; align-items: center; gap: 2px; }
  .spine-text .script { font-size: 42px; }
  .spine-text .caps { font-size: 25px; letter-spacing: 0.02em; }

  /* Front cover */
  .front { position: absolute; left: 624px; top: 0; width: 576px; height: 868px; }
  .front-photo { position: absolute; left: 0; top: 0; width: 576px; height: 340px;
    background: linear-gradient(180deg, var(--sky-deep) 0%, var(--sky-mid) 28%, var(--sky-light) 52%, #55677e 70%, var(--ink) 100%); }
  .front-title { position: absolute; left: 0; width: 576px; top: 268px; text-align: center; }
  .front-title .script { font-size: 150px; }
  .front-title .caps { font-size: 33px; margin-top: -6px; letter-spacing: 0.06em; }
  .subtitle { position: absolute; left: 0; width: 576px; top: 536px; text-align: center; font-size: 16px; line-height: 32.7px; letter-spacing: 0.09em; }
  .author { position: absolute; left: 0; width: 576px; top: 764px; text-align: center; font-size: 46px; letter-spacing: 0.07em; font-weight: 600; }
</style>
</head>
<body>
<div class="cover">

  <section class="back">
    <header class="back-title">
      <div class="script">Lantern Road</div>
      <div class="caps">VENTURES</div>
    </header>

    <div class="blurb">
      <p><span class="lead">LANTERN ROAD VENTURES :</span> Loose Pages of a Harbor Keeper is an honest account of a business owner’s experience attempting to navigate the start-up community while also pursuing spiritual growth. Author Mirela Dunbar defines a spiritual entrepreneur as “someone who runs an enterprise with the purpose of growing love rather than material gain.” This book discusses the three dimensions of Lantern Road Ventures:</p>
      <ol>
        <li>1. The business is an integral part of the founder’s spiritual journey.</li>
        <li>2. Employees working for the spiritual enterprise, whether they know it or not, encounter this company because it's part of their spiritual path.</li>
        <li>3. The business itself has a life force of its own and its purpose is to further the kingdom of heaven on earth.</li>
      </ol>
      <p>These three dimensions happen simultaneously and work together to produce the greatest possible result. However, this can feel confusing to a founder juggling these dimensions while also trying to manage and run a business. This is not a formulaic self-help book or roadmap. Rather, it is a compilation of personal reflections that often seem at odds with the traditional world of entrepreneurship.</p>
    </div>

    <div class="author-photo" role="img" aria-label="Portrait photograph of author Mirela Dunbar outdoors"></div>
    <p class="bio">Mirela Dunbar founded Calveta with the vision of ushering in a life-long education system that shifts away from standardization to one that empowers people to live their purpose. In college, Mirela interned for Open Kettle, a women’s empowerment initiative where she recognized her passion for helping people find their voice. Mirela's 20-year journey has come full circle to empowering other female CEOs who are pursuing the path of Lantern Road Ventures.</p>
  </section>

  <section class="spine">
    <div class="spine-text">
      <span class="script">Lantern Road</span>
      <span class="caps">VENTURES AND MIRELA T. DUNBAR</span>
    </div>
  </section>

  <section class="front">
    <div class="front-photo" role="img" aria-label="Photograph of two climbers silhouetted on a mountain ridge against a bright sunlit sky, one helping the other up"></div>
    <header class="front-title">
      <div class="script">Lantern Road</div>
      <div class="caps">VENTURES</div>
    </header>
    <div class="subtitle caps">LOOSE<br>PAGES<br>OF<br>A<br>HARBOR<br>KEEPER</div>
    <div class="author caps">MIRELA T. DUNBAR</div>
  </section>

</div>
</body>
</html>
```